New Flyer Design Project

Needing brochure explaining the benefits of a home sleep study compared to a clinical hospital sleep study. We had our company logo designed by Lumen Forge, we love it. We would like for it to be a bi-fold. See attachments for examples of information we would like to include.

```html
<!DOCTYPE html>
<html lang="en">
<head>
<meta charset="utf-8">
<title>Northfield Sleep Care – Bi-fold Brochure</title>
<link href="https://fonts.googleapis.com/css2?family=Urbanist:wght@500;600;700&display=swap" rel="stylesheet">
<style>
  :root{
    --green:#5cb946;
    --green-dark:#3f9e3a;
    --blue:#1d4f91;
    --navy:#123a7a;
    --ink:#1f2a3a;
    --grey:#8a8f96;
    --stage:#a9a9a9;
    --paper:#ffffff;
  }
  *{box-sizing:border-box;margin:0;padding:0}
  html,body{width:1200px;height:546px;overflow:hidden}
  body{background:var(--stage);font-family:"Urbanist",sans-serif;color:var(--ink);position:relative}
  .spread{position:absolute;top:63px;width:514px;height:397px;background:var(--paper);overflow:hidden}
  .spread--inside{left:68px}
  .spread--outside{left:619px}
  .spread svg.shapes{position:absolute;inset:0;width:514px;height:397px}
  .abs{position:absolute}

  .brand{font-weight:700;color:var(--blue);font-size:17px;letter-spacing:.2px;display:flex;align-items:center;gap:6px;white-space:nowrap}
  .brand__dot{width:10px;height:10px;border-radius:50%;background:var(--green)}
  .brand--inside{left:62px;top:24px}
  .brand--outside{left:286px;top:292px;font-size:20px}

  .stat{left:22px;top:226px;display:flex;align-items:center;gap:6px;color:var(--green)}
  .stat__num{font-size:33px;font-weight:600;line-height:1}
  .stat__label{font-size:14px;font-weight:700;line-height:1.0}
  .intro{left:22px;top:268px;width:130px;font-size:6px;line-height:1.45;font-weight:500}
  .intro p+p{margin-top:7px}

  .call{left:155px;top:285px;width:92px;height:92px;border-radius:50%;text-align:center;display:flex;flex-direction:column;justify-content:center;color:#fff}
  .call__title{font-size:13px;font-weight:700;color:var(--green)}
  .call__phone{font-size:10px;font-weight:700;margin-top:3px}

  .compare{top:167px;width:110px}
  .compare--home{left:280px}
  .compare--lab{left:398px}
  .compare__head{font-size:10px;font-weight:700;color:var(--blue);margin-bottom:10px;white-space:nowrap}
  .point{position:relative;padding-left:14px;margin-bottom:10px}
  .point__icon{position:absolute;left:0;top:0;width:10px;height:10px}
  .point__title{font-size:9px;font-weight:700;line-height:1.1}
  .compare--home .point__title{color:var(--green)}
  .compare--lab .point__title{color:var(--grey)}
  .point__text{font-size:6px;font-weight:500;line-height:1.35;margin-top:1px}
  .vs{left:370px;top:243px;width:20px;height:20px;border-radius:50%;background:var(--green);color:#fff;font-size:9px;font-weight:700;display:flex;align-items:center;justify-content:center}

  .contact{left:23px;top:256px}
  .contact__head{font-size:13px;font-weight:700;color:var(--green);margin-bottom:7px}
  .contact__row{display:flex;gap:5px;font-size:6px;font-weight:500;line-height:1.4;margin-bottom:5px}
  .contact__row svg{width:7px;height:7px;flex:none;margin-top:1px}
</style>
</head>
<body>

<!-- Inside spread -->
<section class="spread spread--inside">
  <svg class="shapes" viewBox="0 0 514 397" aria-hidden="false">
    <defs>
      <linearGradient id="photoWarm" x1="0" y1="0" x2="1" y2="1">
        <stop offset="0" stop-color="#d8c8b8"/><stop offset=".5" stop-color="#eee8e2"/><stop offset="1" stop-color="#8f8a86"/>
      </linearGradient>
      <linearGradient id="photoBed" x1="0" y1="0" x2="1" y2="1">
        <stop offset="0" stop-color="#e4ddd6"/><stop offset="1" stop-color="#f6f4f2"/>
      </linearGradient>
      <linearGradient id="fold" x1="0" x2="1">
        <stop offset="0" stop-color="#000" stop-opacity=".07"/><stop offset="1" stop-color="#000" stop-opacity="0"/>
      </linearGradient>
      <linearGradient id="band" x1="0" x2="1">
        <stop offset="0" stop-color="#1d4f91"/><stop offset="1" stop-color="#1a6fc0"/>
      </linearGradient>
      <radialGradient id="callFill" cx=".4" cy=".35" r=".7">
        <stop offset="0" stop-color="#1e5aa0"/><stop offset="1" stop-color="#0f336d"/>
      </radialGradient>
    </defs>
    <rect x="257" y="0" width="24" height="397" fill="url(#fold)"/>
    <path role="img" aria-label="Photo: hand wearing a home sleep test finger sensor" d="M0,82 C70,52 160,55 257,112 L257,168 C190,245 70,235 0,182 Z" fill="url(#photoWarm)"/>
    <path d="M0,62 L0,112 L10,88 C80,50 170,55 257,112 C170,40 70,35 0,62 Z" fill="var(--green)"/>
    <path d="M0,186 C75,240 195,238 257,168" fill="none" stroke="var(--blue)" stroke-width="3"/>
    <path role="img" aria-label="Photo: woman sleeping comfortably in bed" d="M257,0 H514 V95 C455,140 375,140 320,120 C295,112 275,104 257,95 Z" fill="url(#photoBed)"/>
    <path d="M257,95 C330,160 450,165 514,95 V112 C445,185 320,165 257,95 Z" fill="var(--green)"/>
    <line x1="380" y1="168" x2="380" y2="352" stroke="#e4e4e4" stroke-width="2"/>
    <path d="M0,365 C120,352 250,356 350,368 C420,376 480,366 514,350 V397 H0 Z" fill="var(--green)"/>
    <path d="M0,376 C150,366 320,378 514,370 V397 H0 Z" fill="url(#band)"/>
    <g fill="var(--green)">
      <circle cx="180" cy="276" r="3.5"/><circle cx="193" cy="273" r="3.8"/><circle cx="206" cy="274" r="4"/>
      <circle cx="220" cy="278" r="5"/><circle cx="234" cy="285" r="5.8"/><circle cx="249" cy="296" r="7"/><circle cx="258" cy="313" r="9"/>
    </g>
    <circle cx="201" cy="331" r="49" fill="#fff"/>
    <circle cx="201" cy="331" r="46" fill="url(#callFill)"/>
    <circle cx="201" cy="331" r="41" fill="none" stroke="var(--green)" stroke-width="1"/>
  </svg>

  <div class="abs brand brand--inside"><span class="brand__dot"></span>Northfield Sleep Care</div>

  <div class="abs stat"><span class="stat__num">80%</span><span class="stat__label">of Sleep Apnea cases<br>go undiagnosed.</span></div>
  <div class="abs intro">
    <p>You wake up exhausted. You fall asleep at your desk. Your partner says you stop breathing at night. You know something's wrong.</p>
    <p>Most people wait years before getting tested because sleep labs are expensive, inconvenient, and scheduled months out. Meanwhile you're crashing your car, destroying your health, and feeling like garbage every single day.</p>
  </div>
  <div class="abs call"><span class="call__title">Call Today!</span><span class="call__phone">555-214-0387</span></div>

  <div class="abs compare compare--home">
    <h2 class="compare__head">Home Sleep Study</h2>
    <div class="point"><svg class="point__icon" viewBox="0 0 10 10"><circle cx="5" cy="5" r="4.5" fill="var(--blue)"/><path d="M2.6,5 L4.4,6.8 L8.8,1.2" fill="none" stroke="var(--green)" stroke-width="1.5"/></svg>
      <div class="point__title">Comfortable</div><div class="point__text">A minimal device with 2<br>wires and 3 sensors</div></div>
    <div class="point"><svg class="point__icon" viewBox="0 0 10 10"><circle cx="5" cy="5" r="4.5" fill="var(--blue)"/><path d="M2.6,5 L4.4,6.8 L8.8,1.2" fill="none" stroke="var(--green)" stroke-width="1.5"/></svg>
      <div class="point__title">Convenient</div><div class="point__text">Delivered to your door -<br>sleep in your own bed at<br>home</div></div>
    <div class="point"><svg class="point__icon" viewBox="0 0 10 10"><circle cx="5" cy="5" r="4.5" fill="var(--blue)"/><path d="M2.6,5 L4.4,6.8 L8.8,1.2" fill="none" stroke="var(--green)" stroke-width="1.5"/></svg>
      <div class="point__title">Accessible</div><div class="point__text">Scheduling and device<br>delivery in 2-4 business days</div></div>
    <div class="point"><svg class="point__icon" viewBox="0 0 10 10"><circle cx="5" cy="5" r="4.5" fill="var(--blue)"/><path d="M2.6,5 L4.4,6.8 L8.8,1.2" fill="none" stroke="var(--green)" stroke-width="1.5"/></svg>
      <div class="point__title">Affordable</div><div class="point__text">Pay a one-time flat fee of<br>$189</div></div>
  </div>

  <div class="abs vs">VS</div>

  <div class="abs compare compare--lab">
    <h2 class="compare__head">Home Sleep Study</h2>
    <div class="point"><svg class="point__icon" viewBox="0 0 10 10"><circle cx="5" cy="5" r="4.5" fill="var(--grey)"/><path d="M3,3 L7,7 M7,3 L3,7" stroke="#fff" stroke-width="1.2"/></svg>
      <div class="point__title">Invasive</div><div class="point__text">20-30 wires attached all<br>over your body</div></div>
    <div class="point"><svg class="point__icon" viewBox="0 0 10 10"><circle cx="5" cy="5" r="4.5" fill="var(--grey)"/><path d="M3,3 L7,7 M7,3 L3,7" stroke="#fff" stroke-width="1.2"/></svg>
      <div class="point__title">Disruptive</div><div class="point__text">Must sleep in a lab<br>overnight and requires<br>travel</div></div>
    <div class="point"><svg class="point__icon" viewBox="0 0 10 10"><circle cx="5" cy="5" r="4.5" fill="var(--grey)"/><path d="M3,3 L7,7 M7,3 L3,7" stroke="#fff" stroke-width="1.2"/></svg>
      <div class="point__title">Hard to Schedule</div><div class="point__text">Scheduling can take<br>anywhere from 3 weeks to<br>6 months</div></div>
    <div class="point"><svg class="point__icon" viewBox="0 0 10 10"><circle cx="5" cy="5" r="4.5" fill="var(--grey)"/><path d="M3,3 L7,7 M7,3 L3,7" stroke="#fff" stroke-width="1.2"/></svg>
      <div class="point__title">Expensive</div><div class="point__text">Fees can range from<br>$500-$10,000</div></div>
  </div>
</section>

<!-- Outside spread -->
<section class="spread spread--outside">
  <svg class="shapes" viewBox="0 0 514 397">
    <defs>
      <linearGradient id="foldOut" x1="0" x2="1">
        <stop offset="0" stop-color="#fff"/><stop offset=".6" stop-color="#f3f3f3"/><stop offset="1" stop-color="#e2e2e2"/>
      </linearGradient>
      <linearGradient id="photoCouple" x1="0" y1="0" x2="1" y2="1">
        <stop offset="0" stop-color="#efe9e2"/><stop offset=".55" stop-color="#d9c8b3"/><stop offset="1" stop-color="#6b84a8"/>
      </linearGradient>
      <linearGradient id="bandOut" x1="0" x2="1">
        <stop offset="0" stop-color="#1a6fc0"/><stop offset="1" stop-color="#1d4f91"/>
      </linearGradient>
      <linearGradient id="dotFade" x1="0" y1="0" x2="1" y2="1">
        <stop offset="0" stop-color="#6cc04a"/><stop offset="1" stop-color="#3fa83d"/>
      </linearGradient>
    </defs>
    <rect x="0" y="0" width="257" height="397" fill="url(#foldOut)"/>
    <path role="img" aria-label="Photo: older couple sleeping peacefully in bed" d="M257,0 H514 V232 C450,226 360,232 257,250 Z" fill="url(#photoCouple)"/>
    <path d="M257,250 C360,232 450,226 514,232 V258 C450,240 360,240 265,252 Z" fill="var(--blue)"/>
    <g fill="url(#dotFade)">
      <circle cx="119" cy="207" r="5.6"/><circle cx="140" cy="203" r="6"/><circle cx="160" cy="203" r="6"/>
      <circle cx="184" cy="208" r="7.5"/><circle cx="206" cy="219" r="9"/><circle cx="229" cy="236" r="11.6"/><circle cx="245" cy="266" r="14.5"/>
    </g>
    <path d="M0,355 C60,385 180,385 300,375 C400,366 470,358 514,365 V397 H0 Z" fill="var(--green)"/>
    <path d="M0,370 C120,388 300,382 514,378 V397 H0 Z" fill="url(#bandOut)"/>
  </svg>

  <div class="abs contact">
    <h2 class="contact__head">Contact Us</h2>
    <div class="contact__row"><svg viewBox="0 0 10 10"><path d="M5,0.5 C2.8,0.5 1.5,2 1.5,3.8 C1.5,6.2 5,9.5 5,9.5 C5,9.5 8.5,6.2 8.5,3.8 C8.5,2 7.2,0.5 5,0.5 Z" fill="var(--blue)"/><circle cx="5" cy="3.8" r="1.3" fill="#fff"/></svg>
      <span>4820 Alder Creek Road<br>Suite 12, Brookfield, MO 63099</span></div>
    <div class="contact__row" style="margin-top:4px"><svg viewBox="0 0 10 10"><path d="M2.2,0.8 L3.8,2.8 L2.9,4 C3.5,5.4 4.6,6.5 6,7.1 L7.2,6.2 L9.2,7.8 L8.1,9.2 C4.5,9 1,5.5 0.8,1.9 Z" fill="var(--blue)"/></svg><span>555-214-0387</span></div>
    <div class="contact__row"><svg viewBox="0 0 10 10"><rect x="0.5" y="3" width="9" height="6" rx="1" fill="var(--blue)"/><rect x="2.5" y="0.8" width="5" height="3" fill="var(--blue)"/><rect x="2" y="5" width="6" height="1" fill="#fff"/></svg><span>555-214-0389</span></div>
  </div>

  <div class="abs brand brand--outside"><span class="brand__dot"></span>Northfield Sleep Care</div>
</section>

</body>
</html>
```